Sponsorenmappe für die Lindenhof Jugend Bewegungs Institut
Zielgruppe
Die Lindenhof Jugend Bewegungs Institut (LJBI) bietet Schulen und Vereinen vielfältige Sport-, Bewegungs- und Ernährungsangebote.
Mit der Lindenhof Jugend Kick Institut (LJKI) und der Jugend Kick Institut (JKI) hat die LJBI-GmbH für den Fußballbereich zwei eigene Marken.
Das ganzheitliche LJBI-Konzept fördert ein sinnvolles Zusammenspiel von Schule, Sport und Persönlichkeitsentwicklung.
Das Design der Sponsorenmappe sollte natürlich in erster Linie den (vorallem mittelständischen) potentiellen Sponsoren gefallen und diese ansprechen. Hier sollte das Design klar und strukturiert sein, jedoch kleine Einflüsse der kinderaffinenen Marken besitzen.
Aufgabenstellung
Anbei haben wir schon einmal eine "Sponsorenmappe" in Word entworfen. Hierbei handelt es sich nur um einen kleinen Vorschlag wie es vielleicht aussehen könnte!
Die Textbausteine sollen jedoch verwendet werden.
Format: Din A4 - Druckdatenblatt von Papierwelle liegt bei.
Vorder- und Rückseite der Broschüre sind schon angefertig! Diese müssen noch noch angefügt werden. Tendenziell sollte die Broschüre dieses Design aufgreifen. Auch die erste Klappseite (Auf dem Druckdatenblatt als "E" gekennzeichnet - bei "D") ist schon designt. Hierbei handelt es sich um das Organigramm der LJBI (siehe Anhang). Überschrift muss jedoch noch in der jeweiligen Schriftart eingefügt werden.
Anbei finden Sie eine Win-Rar-Datei mit Logos und Bildern, die Ihnen zur Verwendung stehen.
Zudem unsere Broschüre für weitere Infos
Dem Rest geben wir küntlerische Freiheit.

```html
<!DOCTYPE html>
<html lang="de">
<head>
<meta charset="utf-8">
<title>Sponsorenmappe – Lindenhof Jugend Bewegungs Institut</title>
<link href="https://fonts.googleapis.com/css2?family=PT+Sans:ital,wght@0,400;0,700;1,400&family=Ubuntu:wght@500;700&display=swap" rel="stylesheet">
<style>
:root{
  --blue:#1a9bd7;
  --cyan:#00a5de;
  --navy:#1c6fa8;
  --green:#5cb030;
  --red:#d52b2b;
  --orange:#f28a1c;
  --yellow:#f1d61e;
  --purple:#6a3a9c;
  --magenta:#e0338f;
  --ink:#1d1d1b;
  --paper:#ffffff;
  --sky:#cfeaf7;
}
*{margin:0;padding:0;box-sizing:border-box}
html,body{width:1006px;height:1200px;overflow:hidden;background:#fff}
body{font-family:"PT Sans",sans-serif;color:var(--ink)}
.canvas{position:relative;width:1006px;height:1200px;overflow:hidden;background:#fff}
.abs{position:absolute}
.sheet{position:absolute;background:var(--paper);box-shadow:3px 5px 7px rgba(0,0,0,.35)}
.photo{position:absolute}
.h-ubuntu{font-family:"Ubuntu",sans-serif;font-weight:700}

/* organigram */
.org-title{left:76px;top:107px;font-family:"Ubuntu",sans-serif;font-weight:500;font-size:12px;color:#fff}
.org-box{position:absolute;background:#fff;border:1.5px solid var(--navy);border-radius:3px;display:flex;align-items:center;justify-content:center;font-family:"Ubuntu",sans-serif;font-weight:500;font-size:7.4px;color:var(--ink);box-shadow:1px 1px 2px rgba(0,0,0,.4)}
.brand{display:flex;align-items:center;gap:4px;font-family:"PT Sans",sans-serif;font-weight:700;color:var(--ink);line-height:1.05;text-transform:uppercase}
.brand .dot{border-radius:50%;border:2px solid var(--blue);flex:none}

/* contact */
.contact-title{left:368px;top:109px;font-family:"Ubuntu",sans-serif;font-weight:700;font-size:10px;color:var(--blue)}
.contact{left:368px;top:129px;font-size:6.8px;line-height:8.9px}
.marks-title{left:369px;top:359px;font-family:"Ubuntu",sans-serif;font-weight:500;font-size:9.5px;color:var(--blue)}

.flap-text{position:absolute;left:354px;top:505px;width:290px;text-align:center;color:#fff;transform:rotate(180deg)}
.flap-text .lead{font-size:7.6px;margin-bottom:3px}
.flap-text .sub{font-size:5.4px;line-height:7px;padding:0 30px}

/* bottom left */
.quote{left:82px;top:810px;width:258px;font-size:4.3px;font-style:italic;line-height:6px}
.quote-src{left:150px;top:825px;width:188px;text-align:right;font-size:3.5px;font-weight:700;text-transform:uppercase}
.general-title{left:83px;top:837px;font-family:"Ubuntu",sans-serif;font-weight:500;font-size:7.2px;color:var(--blue)}
.general-list{left:83px;top:852px;list-style:none;font-size:4.6px;font-style:italic;line-height:9.6px}
.general-list li::before{content:"";display:inline-block;width:3px;height:3px;border-radius:50%;background:var(--green);margin-right:4px;vertical-align:middle}
.tag{position:absolute;background:var(--cyan);color:#fff;font-family:"Ubuntu",sans-serif;font-weight:500;font-size:7.8px;display:flex;align-items:center;justify-content:center}
.pennant{position:absolute;width:75px;height:120px;color:#fff;padding:4px 6px 0}
.pennant h3{font-family:"Ubuntu",sans-serif;font-weight:500;font-size:9px;text-align:center;line-height:10px;margin-bottom:2px}
.pennant p{font-size:3.55px;line-height:4.3px}

/* middle bottom */
.tab{position:absolute;background:var(--cyan);color:#fff;font-family:"Ubuntu",sans-serif;font-weight:700;font-size:7.8px;display:flex;align-items:center;justify-content:center}
.offer{position:absolute;left:371px;width:276px;background:var(--cyan);color:#fff;box-shadow:0 1px 3px rgba(0,0,0,.25)}
.offer h4{position:absolute;left:10px;top:9px;font-family:"Ubuntu",sans-serif;font-weight:700;font-size:6.1px}
.offer .txt{position:absolute;font-size:4.3px;line-height:9.4px}
.chip{position:absolute;height:15px;font-size:4.2px;font-weight:700;display:flex;flex-direction:column;align-items:center;justify-content:center;line-height:5px;text-align:center}
.mini{position:absolute;height:14px;width:19px;font-size:3.4px;font-weight:700;display:flex;flex-direction:column;align-items:center;justify-content:center;line-height:4.4px;text-align:center}
.tilt{position:absolute;border:3px solid #fff;box-shadow:1px 2px 3px rgba(0,0,0,.4)}

/* right bottom */
.level{position:absolute;left:826px;font-family:"Ubuntu",sans-serif;font-weight:700;font-size:8px}
.bubble{position:absolute;border-radius:50%;border:2.5px solid rgba(255,255,255,.9);box-shadow:0 1px 2px rgba(0,0,0,.35);display:flex;align-items:center;justify-content:center;text-align:center;color:#fff;font-family:"Ubuntu",sans-serif;font-weight:700;font-size:5.6px;line-height:6.4px}
.spon{position:absolute;top:992px;height:56px;color:#fff;padding:4px 5px}
.spon h5{font-family:"Ubuntu",sans-serif;font-weight:700;font-size:4.8px;text-align:center;margin-bottom:3px}
.spon ul{list-style:none;font-size:4.4px;line-height:5.6px}
.spon li::before{content:"●";font-size:4px;margin-right:3px}
</style>
</head>
<body>
<div class="canvas">

<!-- ============ OUTER SIDE ============ -->
<svg class="abs" style="left:0;top:0" width="1006" height="600" aria-hidden="true">
  <defs><filter id="sh" x="-5%" y="-5%" width="115%" height="120%"><feDropShadow dx="2" dy="4" stdDeviation="3" flood-opacity=".35"/></filter></defs>
  <polygon points="354,493 644,493 644,544 617,573 381,573 354,544" fill="#2a9ad6" filter="url(#sh)"/>
</svg>
<div class="sheet" style="left:59px;top:86px;width:884px;height:407px"></div>

<!-- Panel: Organigramm -->
<div class="photo" role="img" aria-label="Foto: Trainer und Kinder in grünen Trikots klatschen sich im Kreis ab" style="left:59px;top:86px;width:295px;height:407px;background:linear-gradient(180deg,#5a8fb8 0%,#7cb7d8 22%,#8fcf5a 45%,#7dc24a 70%,#c7cdb5 88%,#7a9a5a 100%)"></div>
<div class="abs org-title">ORGANIGRAMM</div>
<svg class="abs" style="left:59px;top:86px" width="295" height="407" aria-hidden="true">
  <g stroke="#fff" stroke-width="1.3" fill="none">
    <path d="M148 110 V120 M42 130 V120 H254 V130 M113 120 V130 M183 120 V130"/>
    <path d="M148 215 V225 M63 235 V225 H233 V235 M148 225 V260"/>
    <path d="M148 291 V300 M63 308 V300 H233 V308 M148 300 V308"/>
  </g>
</svg>
<div class="org-box" style="left:153px;top:167px;width:108px;height:29px">
  <div class="brand" style="font-size:5.4px"><span class="dot" style="width:15px;height:15px"></span>Lindenhof Jugend<br>Bewegungs Institut GmbH</div>
</div>
<div class="org-box" style="left:71px;top:216px;width:60px;height:30px;font-size:5px">Schulkooperationen</div>
<div class="org-box" style="left:142px;top:216px;width:59px;height:30px">LJBI e.V.</div>
<div class="org-box" style="left:212px;top:216px;width:60px;height:30px">Shop</div>
<div class="org-box" style="left:283px;top:216px;width:59px;height:30px">Marketing</div>
<div class="org-box" style="left:153px;top:272px;width:108px;height:29px">
  <div class="brand" style="font-size:5.4px"><span class="dot" style="width:15px;height:15px"></span>Lindenhof Jugend<br>Kick Institut</div>
</div>
<div class="org-box" style="left:87px;top:321px;width:70px;height:31px">Spezialtraining</div>
<div class="org-box" style="left:257px;top:321px;width:71px;height:31px">Schulungen</div>
<div class="org-box" style="left:171px;top:346px;width:71px;height:31px">
  <div class="brand" style="font-size:6px;color:var(--blue)"><span class="dot" style="width:9px;height:9px;border-color:var(--green)"></span>JKI</div>
</div>
<div class="org-box" style="left:87px;top:394px;width:70px;height:30px">Camps</div>
<div class="org-box" style="left:171px;top:394px;width:71px;height:30px">Reisen</div>
<div class="org-box" style="left:257px;top:394px;width:71px;height:30px">Individualtraining</div>

<!-- Panel: Kontakt -->
<div class="abs contact-title">Kontakt</div>
<div class="abs contact">
  Lindenhof Jugend Bewegungs Institut GmbH<br>
  Geschäftsstelle<br>
  Lindenweg 14<br>
  D- 70000 Musterstadt<br>
  T +49 (0) 7000 123 45 67<br>
  info@ljbi-beispiel.de<br>
  www.ljbi-beispiel.de
</div>
<div class="photo" role="img" aria-label="Foto: Vereinsheim mit Terrasse und Sonnenschirmen auf grüner Wiese unter blauem Himmel" style="left:354px;top:231px;width:290px;height:119px;background:linear-gradient(180deg,#3f8fd6 0%,#8cc3ee 45%,#d9d9d6 62%,#6fa23d 80%,#5b8e2e 100%)"></div>
<div class="abs marks-title">Marken der LJBI-GmbH</div>
<div class="brand abs" style="left:370px;top:398px;font-size:8px;color:var(--blue)"><span class="dot" style="width:14px;height:14px;border-color:var(--green)"></span>JKI</div>
<div class="brand abs" style="left:369px;top:434px;font-size:6.4px"><span class="dot" style="width:24px;height:24px"></span>Lindenhof Jugend<br>Kick Institut</div>

<!-- Panel: Sponsoring cover -->
<div class="photo" style="left:644px;top:86px;width:299px;height:340px;overflow:hidden">
  <svg width="299" height="340" aria-hidden="true">
    <polygon points="0,95 60,80 110,240 0,270" fill="var(--blue)"/>
    <polygon points="110,190 130,185 140,300 118,305" fill="#1e88d0"/>
  </svg>
</div>
<div class="photo" role="img" aria-label="Foto: Kinder in lila Trikots beim Mannschaftsfoto" style="left:644px;top:86px;width:155px;height:95px;background:linear-gradient(180deg,#6bb8c9,#6a3fa0 55%,#4e7f3a)"></div>
<div class="photo" role="img" aria-label="Foto: Fußballschuhe auf Rasen" style="left:800px;top:86px;width:143px;height:80px;background:linear-gradient(160deg,#5c8f3e,#e9e9e9 55%,#3a3a3a)"></div>
<div class="tilt" role="img" aria-label="Foto: Kinderhände aufeinander im Kreis" style="left:655px;top:152px;width:118px;height:92px;transform:rotate(6deg);background:linear-gradient(160deg,#6bbd3e,#3d7a2a 60%,#9bd26a)"></div>
<div class="abs" style="left:720px;top:265px;width:30px;height:135px;background:var(--red);transform:rotate(-12deg)"></div>
<div class="abs" style="left:758px;top:205px;width:25px;height:185px;background:var(--yellow);transform:rotate(-6deg)"></div>
<div class="tilt" role="img" aria-label="Foto: Kinder springen in einen Pool am See" style="left:650px;top:316px;width:122px;height:95px;transform:rotate(-4deg);background:linear-gradient(180deg,#9fcbe8,#7da05a 45%,#3b8fe0 70%,#2f7ad0)"></div>
<div class="tilt" role="img" aria-label="Foto: Trainer und Kinder in grünen Trikots im Kreis" style="left:785px;top:158px;width:158px;height:240px;transform:rotate(3deg);background:linear-gradient(180deg,#4a8ab8,#8fcf5a 40%,#7dc24a 70%,#eeeeee)"></div>
<div class="abs" style="left:661px;top:446px;font-family:'Ubuntu',sans-serif;font-weight:500;font-size:10px">Sponsoring</div>
<div class="brand abs" style="left:800px;top:439px;font-size:6.6px"><span class="dot" style="width:26px;height:26px"></span>Lindenhof Jugend<br>Bewegungs Institut GmbH</div>

<svg class="abs" style="left:0;top:0" width="1006" height="500" aria-hidden="true">
  <g stroke="#e05050" stroke-width=".6" stroke-dasharray="2 2"><line x1="354" y1="86" x2="354" y2="493"/><line x1="644" y1="86" x2="644" y2="493"/></g>
</svg>
<div class="flap-text">
  <div class="lead">Werden Sie Kooperationspartner</div>
  <div class="sub">...der LJBI oder einer unserer Eigenmarken LJKI oder JKI und unterstützen Sie die zahlreichen Vereine, Schulen und Kinder, die von uns betreut werden.</div>
</div>

<!-- ============ INNER SIDE ============ -->
<svg class="abs" style="left:0;top:1040px" width="1006" height="160" aria-hidden="true">
  <defs><filter id="sh2" x="-5%" y="-5%" width="115%" height="130%"><feDropShadow dx="2" dy="4" stdDeviation="3" flood-opacity=".35"/></filter></defs>
  <polygon points="357,26 652,26 652,78 620,109 389,109 357,78" fill="#fff" filter="url(#sh2)"/>
</svg>
<div class="sheet" style="left:59px;top:658px;width:888px;height:408px"></div>

<!-- Left inner panel -->
<svg class="abs" style="left:59px;top:658px" width="392" height="135" role="img" aria-label="Foto: Kinder in lila Trikots laufen jubelnd über den Fußballplatz">
  <defs><linearGradient id="run" x1="0" y1="0" x2="0" y2="1"><stop offset="0" stop-color="#a9c8dc"/><stop offset=".35" stop-color="#6b45a8"/><stop offset=".7" stop-color="#4f2f86"/><stop offset="1" stop-color="#4d8a36"/></linearGradient></defs>
  <path d="M0 0 H390 C300 60 170 110 0 131 Z" fill="url(#run)"/>
  <path d="M0 131 C170 110 300 60 390 0" stroke="var(--navy)" stroke-width="3" fill="none"/>
</svg>
<div class="brand abs" style="left:252px;top:770px;font-size:5.4px"><span class="dot" style="width:20px;height:20px"></span>Lindenhof Jugend<br>Bewegungs Institut GmbH</div>
<p class="abs quote">„Kinder sollten mehr spielen, als viele Kinder es heutzutage tun. Denn wenn man genügend spielt, solange man klein ist, dann trägt man Schätze mit sich herum, aus denen man später sein ganzes Leben lang schöpfen kann."</p>
<div class="abs quote-src">... Greta Holmström (1907 - 2002), Schwedische Schriftstellerin</div>
<div class="abs general-title">Generell gilt</div>
<ul class="abs general-list">
  <li>Kinder bewegen sich weniger und treiben immer seltener Sport</li>
  <li>40-60 % der Kinder haben Haltungsschwächen oder Haltungsschäden</li>
  <li>KIDS-Studie (Kinder in Dauerbewegung Studie) der Hochschule Nordtal</li>
</ul>
<div class="photo" role="img" aria-label="Grafik: hellblaue Silhouette eines Jungen beim Torschuss" style="left:288px;top:845px;width:68px;height:72px;border-radius:40% 50% 45% 40%;background:radial-gradient(ellipse at center,rgba(26,168,224,.55),rgba(26,168,224,0) 70%)"></div>
<div class="tag" style="left:117px;top:889px;width:33px;height:13px">SPAß</div>
<div class="tag" style="left:255px;top:889px;width:50px;height:13px">BEWEGUNG</div>
<div class="brand abs" style="left:169px;top:889px;font-size:3.8px"><span class="dot" style="width:13px;height:13px"></span>Lindenhof Jugend<br>Bewegungs Institut GmbH</div>
<div class="tag" style="left:176px;top:915px;width:64px;height:13px">ENTWICKLUNG</div>
<svg class="abs" style="left:125px;top:904px" width="160" height="26" aria-hidden="true">
  <g fill="var(--cyan)">
    <path d="M6 0 h6 v13 h14 v-5 l9 8 -9 8 v-5 h-20 z"/>
    <path d="M152 0 h-6 v13 h-14 v-5 l-9 8 9 8 v-5 h20 z"/>
  </g>
</svg>
<svg class="abs" style="left:88px;top:936px" width="242" height="124" aria-hidden="true">
  <polygon points="2,0 77,0 77,112 39.5,122 2,112" fill="#1a8fc9"/>
  <polygon points="83,0 158,0 158,112 120.5,122 83,112" fill="var(--green)"/>
  <polygon points="164,0 239,0 239,112 201.5,122 164,112" fill="var(--red)"/>
</svg>
<div class="pennant" style="left:90px;top:937px">
  <h3>Die LJBI</h3>
  <p>bietet vielfältige Sport-, Bewegungs- und Ernährungsangebote. Das ganzheitliche LJBI-Konzept fördert ein sinnvolles Zusammenspiel von Schule, Sport und Persönlichkeitsentwicklung. Spaß und Freude sollen Kinder und Jugendliche langfristig für Sport und Bewegung motivieren. Dabei Eltern entlasten, Kinder fördern, zahlreiche Sport- und Bewegungsangebote schaffen, Gesundheitsschäden vorbeugen und das soziale Verhalten und den Teamgeist der Kinder stärken.</p>
</div>
<div class="pennant" style="left:171px;top:937px">
  <h3>TEAM</h3>
  <p>Die qualifizierten, haupt- und nebenberuflichen Mitarbeiter in den verschiedenen Bereichen der LJBI haben langjährige Erfahrung im Kinder- und Jugendsport. Alle Übungsleiter und Lehrkräfte im Bereich unserer Sportangebote verfügen mindestens über ein<br>● Grundstudium in einem pädagogischen, sozial- oder sportwissenschaftlichen Studiengang<br>● haben eine spezifische Ausbildung oder<br>● Übungsleiter-Lizenz.</p>
</div>
<div class="pennant" style="left:252px;top:937px">
  <h3>PHILOSOPHIE</h3>
  <p>Bei sämtlichen Angeboten der LJBI steht stets der Spaß im Vordergrund. Denn: Wer mit Freude lernt, lernt schneller und nachhaltiger! Neben der sportlichen Ausbildung sollen die Kinder lernen, sich in einer Gruppe zu bewegen, soziale Kontakte zu knüpfen sowie Werte wie Fair Play, Disziplin und Gesundheitsbewusstsein mehr Bedeutung zuzuordnen. Unser Anspruch: hohe Qualität aller angebotenen Leistungen - optimale Beratung, Organisation und Betreuung - gute Zusammenarbeit mit den Kindern, Eltern und Kooperationspartnern.</p>
</div>

<!-- Middle inner panel -->
<div class="tab" style="left:446px;top:665px;width:117px;height:15px">Kompetenzen und Angebote</div>

<div class="offer" style="top:721px;height:106px">
  <h4>CAMPS &amp; SPEZIALTRAINING</h4>
  <div class="txt" style="left:11px;top:18px;width:135px">Teilnahme für Mädchen und Jungen im Alter von 5 bis<br>17 Jahren (verschiedene Altersgruppen) in 2-bis<br>5-Tage-Camps.<br>Camps pro Jahr: .............. 15-20 (2015)<br>Tendenz 2016: ............... 30-40<br>Wie viele Kinder im Schnitt?<br>pro Camp: ...................... 30-40 (2015)<br>Tendenz 2016: ................ 40-50 Regionale</div>
  <div class="abs" style="left:146px;top:44px;display:flex;gap:7px;align-items:center;font-family:'PT Sans',sans-serif;font-weight:700;font-size:5.4px">
    <span style="display:flex;align-items:center;gap:2px"><span style="width:6px;height:6px;border-radius:50%;background:var(--green)"></span>JKI</span>
    <span>Bewegtwerk</span>
    <span style="width:9px;height:9px;background:#2b5e2b"></span>
    <span>Kopfsprung</span>
  </div>
  <div class="txt" style="left:157px;top:70px;line-height:6px">Wahrnehmung eines Camps:</div>
  <div class="chip" style="left:158px;top:85px;width:30px;background:#fff;color:var(--ink)">Personen<br>1500-2500</div>
  <div class="chip" style="left:198px;top:85px;width:29px;background:var(--green)">Flyer 500</div>
  <div class="chip" style="left:235px;top:85px;width:31px;background:var(--red)">Poster 15</div>
</div>
<div class="tilt" role="img" aria-label="Foto: Kinder im Kreis am Strand" style="left:494px;top:686px;width:50px;height:60px;transform:rotate(-6deg);background:linear-gradient(180deg,#9fc4dc,#6c9c4a 55%,#d8c9a3)"></div>
<div class="tilt" role="img" aria-label="Foto: Kinderhände beim Teamkreis" style="left:545px;top:690px;width:50px;height:68px;transform:rotate(5deg);background:linear-gradient(160deg,#6bbd3e,#3d7a2a 60%,#9bd26a)"></div>
<div class="tilt" role="img" aria-label="Foto: Beachsoccer am Meer" style="left:593px;top:680px;width:50px;height:68px;transform:rotate(-8deg);background:linear-gradient(180deg,#8fb7d8,#a9c4d6 50%,#e3d6b6)"></div>

<div class="offer" style="top:833px;height:104px">
  <h4>REISEN</h4>
  <div class="txt" style="left:10px;top:18px;width:125px">In Kooperation mit unseren Reisepartnern Sonnenflug Reisen und Reisewerk Nord veranstaltet die JKI Reisen ins Ausland in Verbindung mit Fußballcamps. Professionelle Mitarbeiter, Trainer und Betreuer der Lindenhof Jugend Kick Institut (LJKI) sind bei den Camps vor Ort.</div>
  <div class="txt" style="left:145px;top:18px;width:125px">Tendenz 2016:<br><span style="padding-left:31px">8 Camps</span><br><span style="padding-left:31px">25-30 Teilnehmer pro Reise</span><br><span style="padding-left:31px">Türkei, Mallorca, Deutschland…</span><br>Akquise von Teilnehmern:</div>
  <div class="mini" style="left:145px;top:84px;background:var(--green)">Kataloge<br>150.000</div>
  <div class="mini" style="left:168px;top:84px;background:#fff;color:var(--ink)">Messen<br>2-3</div>
  <div class="mini" style="left:191px;top:84px;background:var(--red)">Camps<br>30-40</div>
  <div class="mini" style="left:214px;top:84px;background:var(--green)">Flyer<br>ca. 5.000</div>
  <div class="abs" style="left:15px;top:86px;width:13px;height:13px;background:#f3c400"></div>
  <div class="abs" style="left:37px;top:86px;width:14px;height:14px;border-radius:50%;background:#5aa9d6"></div>
</div>

<div class="offer" style="top:943px;height:105px">
  <h4>SCHULKOOPERATIONEN</h4>
  <div class="txt" style="left:10px;top:18px;width:130px">Die LJBI bietet Schulen kostenfreie und ganzheitliche Konzepte sowie umfangreiche, sportartübergreifende und sportartspezifische Angebote in folgenden Bereichen an:<br>▪ Schulsport-Arbeitsgemeinschaften (AGs)<br>▪ Schulsporttage<br>▪ Schulturniere und -veranstaltungen<br>▪ Gesundheit, Prävention und Ernährung</div>
  <div class="txt" style="left:150px;top:18px;width:120px">Sporttage 2015: ..................10 - 15<br>Tendenz 2016: ................ 40 - 60<br>So wurden 2015 etwa 400-600 Kinder für eine aktive Lebensweise begeistert</div>
</div>
<div class="tilt" role="img" aria-label="Foto: Kinder beim Gruppenspiel in der Halle" style="left:534px;top:1000px;width:55px;height:68px;transform:rotate(-7deg);background:linear-gradient(180deg,#d9d9e6,#6a3fa0 50%,#b66a4a)"></div>
<div class="tilt" role="img" aria-label="Foto: Schulsporttag auf dem Rasenplatz" style="left:588px;top:995px;width:52px;height:64px;transform:rotate(8deg);background:linear-gradient(180deg,#b9c9a3,#6ba23d 45%,#d24a3a)"></div>

<!-- Right inner panel -->
<div class="tab" style="left:656px;top:666px;width:181px;height:15px">Sponsoringmöglichkeiten bei der LJBI</div>
<svg class="abs" style="left:665px;top:690px" width="142" height="116" aria-hidden="true">
  <defs><clipPath id="pyr"><polygon points="71,0 142,116 0,116"/></clipPath></defs>
  <g clip-path="url(#pyr)">
    <rect y="0" width="142" height="19" fill="var(--purple)"/>
    <rect y="20" width="142" height="18" fill="var(--magenta)"/>
    <rect y="39" width="142" height="18" fill="var(--red)"/>
    <rect y="58" width="142" height="18" fill="var(--orange)"/>
    <rect y="77" width="142" height="18" fill="var(--yellow)"/>
    <rect y="96" width="142" height="20" fill="#2f9a3e"/>
  </g>
</svg>
<div class="level" style="top:696px;color:var(--purple)">HAUPTSPONSOR</div>
<div class="level" style="top:716px;color:var(--magenta)">PREMIUM PARTNER</div>
<div class="level" style="top:735px;color:var(--red)">TOP PARTNER</div>
<div class="level" style="top:754px;color:var(--orange)">PARTNER</div>
<div class="level" style="top:773px;color:var(--yellow)">UNTERSTÜTZER</div>
<div class="level" style="top:792px;color:#2f9a3e">FÖRDERER</div>

<div class="photo" role="img" aria-label="Grafik: hellblaue Silhouetten jubelnder Kinder" style="left:652px;top:945px;width:295px;height:121px;background:linear-gradient(180deg,rgba(207,234,247,0),var(--sky) 30%)"></div>
<div class="photo" role="img" aria-label="Grafik: blaue Silhouette eines Kindes mit Ball" style="left:893px;top:806px;width:30px;height:75px;border-radius:45%;background:radial-gradient(ellipse,rgba(26,168,224,.6),rgba(26,168,224,0) 70%)"></div>
<div class="tilt" role="img" aria-label="Foto: Hand zeichnet Spieltaktik auf eine Tafel" style="left:669px;top:823px;width:68px;height:86px;transform:rotate(6deg);background:linear-gradient(160deg,#3a3a3a,#1f1f1f 70%,#c9a38a)"></div>
<div class="tilt" role="img" aria-label="Foto: Kinder in der Gruppe beim Training" style="left:663px;top:928px;width:68px;height:50px;transform:rotate(-4deg);background:linear-gradient(180deg,#7fb3d8,#6bbd3e 55%,#3d7a2a)"></div>
<div class="tilt" role="img" aria-label="Foto: Beachsoccer-Turnier am See" style="left:875px;top:900px;width:68px;height:82px;transform:rotate(7deg);background:linear-gradient(180deg,#6aa5d8,#a9c4d6 50%,#e3d6b6)"></div>

<div class="bubble" style="left:760px;top:831px;width:38px;height:38px;background:#2a9a4a">REISEN</div>
<div class="bubble" style="left:815px;top:831px;width:38px;height:38px;background:var(--purple)">EVENTS</div>
<div class="bubble" style="left:737px;top:865px;width:38px;height:38px;background:#4a3a9c">MESSEN</div>
<div class="bubble" style="left:837px;top:865px;width:38px;height:38px;background:#1aa6c9">SCHUL<br>TAGE</div>
<div class="bubble" style="left:783px;top:873px;width:46px;height:46px;background:var(--orange);font-size:13px;line-height:13px;font-weight:500">CSR</div>
<div class="bubble" style="left:737px;top:909px;width:38px;height:38px;background:var(--magenta)">CAMPS</div>
<div class="bubble" style="left:837px;top:909px;width:38px;height:38px;background:#d11f2a">SOCCER<br>COURT</div>
<div class="bubble" style="left:787px;top:931px;width:38px;height:38px;background:#d8c52a;font-size:5px">SPEZIAL-<br>TRAINING</div>
<div class="abs" style="left:879px;top:868px;width:18px;height:18px;border-radius:50%;background:var(--cyan)"></div>

<div class="spon" style="left:665px;width:65px;background:#1aa34a"><h5>WERBEBANNER</h5><ul><li>Beachflags</li><li>Beachbanner</li><li>Bandenwerbung</li><li>Sponsorenwand</li></ul></div>
<div class="spon" style="left:736px;width:64px;background:var(--orange)"><h5>NEUE MEDIEN</h5><ul><li>Homepagebanner</li><li>Sponsorenpyramide</li><li>Social Media-Werbung</li></ul></div>
<div class="spon" style="left:806px;width:65px;background:var(--cyan)"><h5>AUSRÜSTUNG</h5><ul><li>Trikots</li><li>Hosen</li><li>Bälle</li><li>Trinkflaschen, etc.</li></ul></div>
<div class="spon" style="left:876px;width:66px;background:var(--magenta)"><h5>PRINTMEDIEN</h5><ul><li>Poster</li><li>Flyer</li><li>Werbeanzeigen</li><li>Infomaterial</li></ul></div>

</div>
</body>
</html>
```